Name card design for KOV mobile accessories company

KOV is an upmarket brand, we are looking for professional business card design.

the design should be neat and simple but giving a strong feeling.
should not be colorful. make it black/white/gray tone

Name:
Job title:
Contact no.:
company address: i would like the company address to be very small and thin.
link to social media profile:
company website:

*the company have no website yet
as the project is done please i also would like the font that use in design as well; for more further people in company need a business card:)
Updates

Thank you for all super fast submission :D they're all look cool!

i have just update my brief to make the statement clearer, please check it out :)
if you have any question please dont hesitate to ask.
i would like see more design from you! 
Keep it up!  :D

Target Market(s)

Company target are upmarket company distributor, such as Vordane and Pilto store.

Industry/Entity Type

Business

Font styles to use
Serif
Sans Serif
Other font styles liked:
• Formal and mordern

Colors
ffffff
eeeeee
d3d3d3
919191
474747
1b1b1b
000000
333333

Requirements
Must have
• The design must be professional clean and clear but also Strong and Modern!
text should be formal and mordern
Should not have
• No complicated design!

```html
<!DOCTYPE html>
<html lang="en">
<head>
<meta charset="UTF-8">
<title>KOV Business Card</title>
<link href="https://fonts.googleapis.com/css2?family=Exo+2:wght@300;400;500&display=swap" rel="stylesheet">
<style>
  :root {
    --white: #ffffff;
    --paper: #eeeeee;
    --panel: #2f2f2f;
    --ink: #1b1b1b;
    --black: #000000;
    --mid: #919191;
    --stage: #d3d3d3;
  }
  * { margin: 0; padding: 0; box-sizing: border-box; }
  html, body {
    width: 1200px; height: 821px; overflow: hidden;
    background: var(--stage);
    font-family: "Exo 2", sans-serif;
  }
  .sheet {
    width: 1200px; height: 821px;
    display: flex; align-items: center; justify-content: center; gap: 40px;
  }
  .card {
    position: relative;
    width: 520px; height: 297px;
    background: var(--white);
    overflow: hidden;
    box-shadow: 0 6px 18px rgba(0,0,0,0.18);
  }
  /* front */
  .card-front__panel {
    position: absolute; left: 180px; top: 0; right: 0; height: 228px;
    background: var(--panel);
  }
  .card-front__name {
    position: absolute; top: 30px; left: 0; right: 0;
    font-size: 25px; font-weight: 500; letter-spacing: 2px; line-height: 1;
  }
  .name-first { position: absolute; right: 350px; color: var(--ink); }
  .name-last { position: absolute; left: 196px; color: var(--white); }
  .card-front__title {
    position: absolute; left: 196px; top: 60px;
    color: var(--white); font-size: 11px; font-weight: 400; letter-spacing: 1.5px;
  }
  .contact-list {
    position: absolute; left: 180px; top: 92px; list-style: none;
  }
  .contact-item {
    display: flex; align-items: center; height: 32px;
    color: var(--white); font-size: 12.5px; font-weight: 300; letter-spacing: 0.6px;
  }
  .contact-item__icon {
    width: 24px; height: 24px; background: var(--black);
    display: flex; align-items: center; justify-content: center;
    margin-right: 14px; flex: none;
  }
  .contact-item__icon svg { width: 13px; height: 13px; }
  .contact-item--address { line-height: 1.15; font-size: 11.5px; }
  .card-front__brand {
    position: absolute; left: 28px; bottom: 18px;
    width: 140px;
  }
  .brand-name {
    display: block;
    font-size: 54px; font-weight: 500; letter-spacing: 4px; line-height: 1;
    color: var(--ink);
  }
  /* back */
  .card-back__field {
    position: absolute; inset: 12px;
    background: var(--panel);
  }
</style>
</head>
<body>
<main class="sheet">
  <section class="card card-front">
    <div class="card-front__panel"></div>
    <div class="card-front__name">
      <span class="name-first">TOMAS</span>
      <span class="name-last">REYKE</span>
    </div>
    <div class="card-front__title">FINANCIAL ADVISOR</div>
    <ul class="contact-list">
      <li class="contact-item contact-item--address">
        <span class="contact-item__icon">
          <svg viewBox="0 0 16 16"><path d="M8 1a5 5 0 0 0-5 5c0 4 5 9 5 9s5-5 5-9a5 5 0 0 0-5-5zm0 7a2 2 0 1 1 0-4 2 2 0 0 1 0 4z" fill="#fff"/></svg>
        </span>
        <span>0417 9th floor,Marrow Lane<br>Road KTP</span>
      </li>
      <li class="contact-item">
        <span class="contact-item__icon">
          <svg viewBox="0 0 16 16"><path d="M4 1l3 3-2 2c1 2 3 4 5 5l2-2 3 3-2 2C7 14 2 9 2 3z" fill="#fff"/></svg>
        </span>
        <span>014 528 3096</span>
      </li>
      <li class="contact-item">
        <span class="contact-item__icon">
          <svg viewBox="0 0 16 16"><rect x="1.5" y="3.5" width="13" height="9" fill="none" stroke="#fff" stroke-width="1.4"/><path d="M1.5 3.5l6.5 5 6.5-5" fill="none" stroke="#fff" stroke-width="1.4"/></svg>
        </span>
        <span>tomas@kovmail.com</span>
      </li>
      <li class="contact-item">
        <span class="contact-item__icon">
          <svg viewBox="0 0 16 16" fill="none" stroke="#fff" stroke-width="1.2"><circle cx="8" cy="8" r="6.5"/><ellipse cx="8" cy="8" rx="3" ry="6.5"/><path d="M1.5 8h13M2.5 4.5h11M2.5 11.5h11"/></svg>
        </span>
        <span>www.kovstore.com</span>
      </li>
    </ul>
    <div class="card-front__brand">
      <span class="brand-name">KOV</span>
    </div>
  </section>

  <section class="card card-back">
    <div class="card-back__field"></div>
  </section>
</main>
</body>
</html>
```